Vibrant box design for eco coconut shell herb growing kit

We are looking for vibrant and standout packaging designs for PlantiNut - our herb growing kits made from coconut by-products.
First and foremost, the packaging needs to look great on a shelf, with lots of colour, in a way that stands out communicates what our product is. It should reflect both the fun nature of the brand but also our strong eco ethos and appeal as much to adults as it does to kids as we target the home interior market, as well as an eco-friendly/green-fingered one. I love bold colours and shapes in a modern, almost retro Y2K style but also love the idea of southeast Asian/mandala inspired patterns being included on the packaging – I’d like for one or the other to be used, likely not both! We will be looking for 2 designs which should be of matching designs but have a colour difference, either of the whole box or part of it, one for Greek Basil, and one for Corsican Mint. It should be so that the same colour difference can be applied to new products as they are introduced. I.e Mint is a pale blue, basil is green, and we could have sage as purple etc etc in future.
The box is a simple 10x10x10.5cm cube and I have a strong idea on what should be on 2 of the faces. The front is to include a semicircle cut-out to reveal the coconut shell inside, no less than 3cm from the base of the box (this is included on the die-lines but needs to be moved upwards), with the logo above it, and a stylised depiction of Corsican Mint/Greek Basil which spills over the upper edge to give the impression it is ‘growing’ from the pot – with a cut around so this pops up when on a shelf ( See reference photo of my mock-up).
One of the other sides should be at least half dedicated to a space to write a message.
As this is something we are looking to sell both online and in stores, there are several other requirements to incorporate into the design and I will happily provide more information on request so these can be added.
Target Market(s)
The target market is for UK garden centres, and so green-fingered adults, but should also appeal to kids
Look and feel

```html
<!DOCTYPE html>
<html lang="en">
<head>
<meta charset="utf-8">
<title>PlantiNut Greek Basil Growing Kit – Box Dieline</title>
<link href="https://fonts.googleapis.com/css2?family=Caveat+Brush&family=Fredoka:wght@600&family=Kalam:wght@300;400&family=Roboto:wght@500&display=swap" rel="stylesheet">
<style>
  :root {
    --basil-dark: #4f8d3e;
    --basil-light: #acd46c;
    --basil-text: #5d9a40;
    --earth: #b5522a;
    --pattern-teal: #4aa7a0;
    --pattern-lime: #c9df6a;
    --crease: #e8333c;
    --cut: #9b3a3a;
    --ink: #222222;
    --paper: #ffffff;
    --guide: #3fb0e6;
  }
  * { margin: 0; padding: 0; box-sizing: border-box; }
  html, body { width: 839px; height: 1200px; overflow: hidden; background: var(--paper); }
  .canvas { position: relative; width: 839px; height: 1200px; font-family: "Kalam", cursive; }
  .dieline { position: absolute; left: 0; top: 0; }
  .abs { position: absolute; }

  .legend-label { font-family: "Roboto", sans-serif; font-weight: 500; font-size: 15px; }
  .legend-label--crease { color: var(--crease); left: 78px; top: 107px; }
  .legend-label--cut { color: var(--ink); left: 78px; top: 146px; }

  .dimension { font-family: "Roboto", sans-serif; font-size: 14px; color: var(--ink); background: var(--paper); padding: 0 3px; }

  .info-copy { left: 68px; top: 262px; width: 160px; font-size: 7.2px; line-height: 12px; font-style: italic; text-align: justify; color: var(--ink); }
  .info-copy p + p { margin-top: 5px; }
  .brand-name { font-family: "Kalam", cursive; font-weight: 300; white-space: nowrap; }
  .brand-name--info { left: 68px; top: 366px; font-size: 11px; color: var(--basil-text); }
  .small-print { left: 67px; top: 386px; width: 85px; font-family: "Roboto", sans-serif; font-weight: 400; font-size: 4.6px; line-height: 9px; color: var(--ink); }

  .title-greek { left: 272px; top: 248px; font-family: "Caveat Brush", cursive; font-size: 56px; color: var(--paper); line-height: 1; }
  .title-basil { left: 296px; top: 300px; font-family: "Caveat Brush", cursive; font-size: 60px; color: var(--basil-dark); line-height: 1; }
  .kit-label { font-family: "Fredoka", sans-serif; font-weight: 600; color: var(--earth); letter-spacing: 0.5px; white-space: nowrap; }
  .kit-label--side { left: 240px; width: 183px; top: 369px; text-align: center; font-size: 16px; }

  .brand-name--front { left: 423px; width: 184px; top: 286px; text-align: center; font-size: 19px; color: var(--basil-text); }
  .seed-badge { left: 434px; top: 395px; width: 30px; height: 28px; border-radius: 50%; background: var(--basil-dark); color: var(--paper); text-align: center; font-family: "Fredoka", sans-serif; font-weight: 600; }
  .seed-badge .weight { display: block; font-size: 8px; line-height: 10px; margin-top: 3px; }
  .seed-badge .caption { display: block; font-size: 3.6px; line-height: 4.2px; }
  .front-title { left: 504px; top: 385px; font-family: "Caveat Brush", cursive; font-size: 24px; color: var(--basil-text); line-height: 1; white-space: nowrap; }
  .kit-label--front { left: 538px; top: 412px; font-size: 8px; }

  .brand-name--story { left: 607px; width: 184px; top: 252px; text-align: center; font-size: 18px; color: var(--paper); }
  .story-copy { left: 626px; top: 283px; width: 148px; font-size: 8.3px; line-height: 12px; font-style: italic; text-align: justify; color: var(--basil-text); }
</style>
</head>
<body>
<div class="canvas">
  <svg class="dieline" width="839" height="1200" viewBox="0 0 839 1200" xmlns="http://www.w3.org/2000/svg">
    <defs>
      <linearGradient id="basilFoliage" x1="0" y1="0" x2="0" y2="1">
        <stop offset="0" stop-color="#e9f4dc"/>
        <stop offset="1" stop-color="#b9d99a"/>
      </linearGradient>
    </defs>

    <!-- legend -->
    <rect x="31" y="113" width="40" height="7" fill="var(--crease)"/>
    <rect x="31" y="152" width="40" height="7" fill="#3a3a3a"/>

    <!-- lid flap -->
    <path d="M423 60 V45 Q423 25 443 25 H587 Q607 25 607 45 V60" fill="none" stroke="var(--cut)" stroke-width="0.8"/>
    <rect x="423" y="60" width="184" height="184" fill="var(--basil-dark)"/>

    <!-- dust flaps -->
    <path d="M240 244 V233 L249 225 L264 162 H400 L423 244" fill="none" stroke="var(--cut)" stroke-width="0.8"/>
    <path d="M607 244 L631 162 H767 L782 225 L791 233 V244" fill="none" stroke="var(--cut)" stroke-width="0.8"/>
    <path d="M56 244 L23 265 V419 L56 437" fill="none" stroke="var(--cut)" stroke-width="0.8"/>

    <!-- bottom flaps -->
    <path d="M56 437 L113 527 V546 Q113 550 117 550 H179 Q183 550 183 546 V527 L240 437" fill="none" stroke="var(--cut)" stroke-width="0.8"/>
    <path d="M240 437 L244 527 H325 Q345 520 332 493 L423 437" fill="none" stroke="var(--cut)" stroke-width="0.8"/>
    <path d="M423 437 V550 H474 Q478 550 478 546 L479 528 H552 L556 546 Q557 550 561 550 H607 V437" fill="none" stroke="var(--cut)" stroke-width="0.8"/>
    <path d="M607 437 L698 493 Q685 520 705 527 H787 V437" fill="none" stroke="var(--cut)" stroke-width="0.8"/>

    <!-- side panel with title -->
    <rect x="240" y="244" width="183" height="151" fill="var(--basil-light)"/>
    <rect x="240" y="395" width="183" height="36" fill="var(--pattern-teal)" role="img" aria-label="Band of woven diamond pattern in teal, lime and rust"/>
    <rect x="240" y="395" width="183" height="4" fill="var(--earth)"/>
    <rect x="240" y="431" width="183" height="6" fill="var(--earth)"/>

    <!-- story panel -->
    <rect x="607" y="244" width="184" height="151" fill="var(--basil-light)"/>
    <rect x="607" y="395" width="184" height="36" fill="var(--pattern-teal)" role="img" aria-label="Band of woven diamond pattern in teal, lime and rust"/>
    <rect x="607" y="395" width="184" height="4" fill="var(--earth)"/>
    <rect x="607" y="431" width="184" height="6" fill="var(--earth)"/>

    <!-- front panel -->
    <rect x="423" y="244" width="184" height="193" fill="var(--paper)"/>
    <rect x="423" y="431" width="184" height="6" fill="var(--earth)"/>
    <path d="M448 196 Q452 188 464 192 Q478 184 492 194 Q506 186 520 194 Q540 184 556 196 Q574 190 584 206 Q590 222 584 240 V310 H458 V250 Q440 232 448 196 Z" fill="url(#basilFoliage)" stroke="var(--paper)" stroke-width="2" role="img" aria-label="Line illustration of basil sprigs growing up and over the top edge"/>
    <path d="M446 313 H584 A69 69 0 0 1 446 313 Z" fill="var(--paper)" stroke="var(--ink)" stroke-width="0.9"/>

    <!-- crease lines -->
    <g fill="none" stroke="var(--crease)" stroke-width="0.8">
      <rect x="56" y="244" width="735" height="193"/>
      <line x1="240" y1="244" x2="240" y2="437"/>
      <line x1="423" y1="60" x2="423" y2="437"/>
      <line x1="607" y1="60" x2="607" y2="437"/>
      <line x1="423" y1="60" x2="607" y2="60"/>
    </g>

    <!-- message box -->
    <rect x="161" y="379" width="68" height="48" fill="none" stroke="var(--ink)" stroke-width="0.9"/>

    <!-- dimensions -->
    <g stroke="var(--guide)" stroke-width="0.5" fill="var(--guide)">
      <line x1="56" y1="190" x2="56" y2="244"/>
      <line x1="240" y1="190" x2="240" y2="244"/>
      <line x1="56" y1="203" x2="240" y2="203"/>
      <path d="M56 203 l6 -2.5 v5 z M240 203 l-6 -2.5 v5 z"/>
      <line x1="240" y1="437" x2="240" y2="585"/>
      <line x1="423" y1="550" x2="423" y2="585"/>
      <line x1="240" y1="576" x2="423" y2="576"/>
      <path d="M240 576 l6 -2.5 v5 z M423 576 l-6 -2.5 v5 z"/>
      <line x1="791" y1="244" x2="818" y2="244"/>
      <line x1="791" y1="437" x2="818" y2="437"/>
      <line x1="812" y1="244" x2="812" y2="437"/>
      <path d="M812 244 l-2.5 6 h5 z M812 437 l-2.5 -6 h5 z"/>
    </g>
  </svg>

  <div class="abs legend-label legend-label--crease">Crease line</div>
  <div class="abs legend-label legend-label--cut">Cutting line</div>

  <div class="abs dimension" style="left:114px; top:194px;">10.00 cm</div>
  <div class="abs dimension" style="left:298px; top:567px;">10.00 cm</div>
  <div class="abs dimension" style="left:774px; top:331px; transform: rotate(-90deg);">10.50 cm</div>

  <div class="abs info-copy">
    <p>Each kit includes everything you need to start your very own herb garden: organic coconut fiber pots, nutrient-rich soil infused with coconut husk fibers, and a carefully selected assortment of herb seeds.</p>
    <p>Contents: 2.5g organic seed packet, 20g soil, coconut shell.</p>
  </div>
  <div class="abs brand-name brand-name--info">PlantiNut</div>
  <div class="abs small-print">Lorem ipsum dolor sit amet, consectetuer adipiscing elit, sed diam nonummy nibh euismod tincidunt ut</div>

  <div class="abs title-greek">Greek</div>
  <div class="abs title-basil">Basil</div>
  <div class="abs kit-label kit-label--side">GROWING KIT</div>

  <div class="abs brand-name brand-name--front">PlantiNut</div>
  <div class="abs seed-badge"><span class="weight">2.5G</span><span class="caption">SEED<br>PACKAGE</span></div>
  <div class="abs front-title">Greek Basil</div>
  <div class="abs kit-label kit-label--front">GROWING KIT</div>

  <div class="abs brand-name brand-name--story">PlantiNut</div>
  <div class="abs story-copy">Embrace the essence of sustainability and bring a touch of green to your kitchen or outdoor space. Whether you're a seasoned green thumb or a novice gardener, our coconut-based herb growing kits provide a hassle-free and environmentally friendly solution for cultivating your own herbs.</div>
</div>
</body>
</html>
```